Business Card Design for VELMOR Technology Partners

already have logo. I am showing existing card so you can see address/phone info this design needs to be simple,clean,creative

```html
<!DOCTYPE html>
<html lang="en">
<head>
<meta charset="UTF-8">
<title>VELMOR Technology Partners – Business Card</title>
<link rel="stylesheet" href="https://fonts.googleapis.com/css2?family=Tinos&family=Michroma&family=Open+Sans:ital,wght@0,400;1,400&display=swap">
<style>
  :root {
    --backdrop: #aeb1b9;
    --card: #ffffff;
    --navy: #1d3a8a;
    --ink: #1c2a4a;
    --text: #2b2b35;
    --rule: #8a8f99;
    --accent: #2f7fc0;
  }
  * { margin: 0; padding: 0; box-sizing: border-box; }
  html, body { width: 1200px; height: 800px; overflow: hidden; }
  body { background: var(--backdrop); position: relative; font-family: "Open Sans", sans-serif; }

  .card {
    position: absolute;
    width: 576px;
    height: 327px;
    background: var(--card);
    border-radius: 10px;
    overflow: hidden;
  }
  .card--front { left: 96px; top: 69px; }
  .card--back { left: 533px; top: 451px; }

  .band { position: absolute; left: 0; width: 100%; }
  .band--top { top: 0; height: 24px; }
  .band--bottom { bottom: 0; height: 36px; }

  .brand-mark { position: absolute; border-radius: 50%; background: var(--accent); }
  .brand-name {
    position: absolute;
    font-family: "Tinos", serif;
    color: var(--ink);
    letter-spacing: 1px;
  }

  .front-mark { width: 64px; height: 64px; left: 256px; top: 46px; }
  .front-name { left: 0; width: 100%; text-align: center; top: 120px; font-size: 38px; }
  .tagline {
    position: absolute; left: 0; width: 100%; top: 160px;
    text-align: center; font-family: "Tinos", serif; font-size: 18px; color: var(--text);
  }
  .web-rule { position: absolute; top: 272px; left: 0; width: 100%; display: flex; align-items: center; }
  .web-rule .line { flex: 1; height: 1px; background: var(--rule); }
  .web-rule .line--left { margin-left: 4px; }
  .web-rule .url { padding: 0 14px; font-size: 18px; color: #3d4352; }

  .back-mark { width: 70px; height: 70px; left: 10px; top: 20px; }
  .back-name { left: 92px; top: 32px; font-size: 40px; }
  .holder { position: absolute; left: 328px; top: 112px; }
  .holder .person {
    font-family: "Michroma", sans-serif; font-size: 21px;
    letter-spacing: 3px; color: var(--ink); text-transform: uppercase;
  }
  .holder .role { font-size: 15px; color: var(--text); margin-top: 4px; }
  .holder .email { font-size: 15px; font-style: italic; color: var(--text); margin-top: 2px; }
  .office { position: absolute; left: 10px; top: 248px; color: var(--text); }
  .office .company { font-size: 16px; }
  .office .line-sm { font-size: 11px; margin-top: 4px; }
  .back-url {
    position: absolute; right: 8px; bottom: 4px;
    font-size: 18px; font-style: italic; color: #ffffff;
  }
</style>
</head>
<body>
  <section class="card card--front">
    <svg class="band band--top" viewBox="0 0 576 24" preserveAspectRatio="none">
      <polygon points="0,0 576,0 576,22 0,12" fill="var(--navy)"/>
      <polyline points="0,14 560,18 576,24" fill="none" stroke="#ffffff" stroke-width="2"/>
    </svg>
    <span class="brand-mark front-mark"></span>
    <div class="brand-name front-name">VELMOR</div>
    <p class="tagline">Technology Strategy | IT Service Management</p>
    <div class="web-rule">
      <span class="line line--left"></span>
      <span class="url">www.velmor.com</span>
      <span class="line"></span>
    </div>
  </section>

  <section class="card card--back">
    <span class="brand-mark back-mark"></span>
    <div class="brand-name back-name">VELMOR</div>
    <div class="holder">
      <div class="person">Daniel Hartwell</div>
      <div class="role">Designation</div>
      <div class="email">daniel.hartwell@velmor.com</div>
    </div>
    <div class="office">
      <div class="company">VELMOR Technology Services</div>
      <div class="line-sm">48, 9th Avenue Fremont, CA-94538.</div>
      <div class="line-sm">510-555-0148</div>
    </div>
    <svg class="band band--bottom" viewBox="0 0 576 36" preserveAspectRatio="none">
      <polygon points="0,24 576,0 576,36 0,36" fill="var(--navy)"/>
      <polyline points="0,22 576,-2" fill="none" stroke="#ffffff" stroke-width="2"/>
    </svg>
    <span class="back-url">www.velmor.com</span>
  </section>
</body>
</html>
```